Velorin Biotechnology needs a professional powerpoint design

We would like to re-design our powerpoint template(as attachment 1), it should be based on our current logo (as attachment 2). We hope the new powerpoint template could be more professional and like a biotechnology company with advanced technology.
Velorin Biotechnology is a contract development and manufacturing organization to provide high quality services to our clients in development, lead-in advanced technology and cGMP manufacturing of biopharmaceuticals from clinical to commercial manufacturing. We offers the advanced technology and services to become the best partner for clients from clinical to commercial manufacturing.
Reason: We would like to extend the deadline for this project so that designers can have more time to prepare, thanks.
Target Market(s)
Velorin Biotechnology is a contract development and manufacturing organization to provide high quality services to our clients in development, lead-in advanced technology and cGMP manufacturing of biopharmaceuticals from clinical to commercial manufacturing.
Velorin primary focus on development and manufacturing of glycoprotein pharmaceuticals against breast cancer, supplies KEV Taiwan with KEV-347 & KEV-348 for global clinical trials and commercialization in the future. Velorin offers the advanced technology and services to become the best partner for clients from clinical to commercial manufacturing.
Industry/Entity Type
Biotechnology
Requirements
Must have
- The new powerpoint design should based on our current logo.
Should not have
- The similar design with current powerpoint style. Please don't refer the design style of our current website http://www.velorin-example.com.tw/ as well, we will re-design it soon.

```html
<!DOCTYPE html>
<html lang="en">
<head>
<meta charset="utf-8">
<title>Velorin Biotechnology – Title Slide</title>
<link rel="stylesheet" href="https://fonts.googleapis.com/css2?family=Roboto:wght@700&display=swap">
<style>
  :root {
    --paper: #ffffff;
    --mist: #e9ebea;
    --footer-band: #d2d3d3;
    --green-deep: #0c4a2b;
    --green-mid: #1b7d45;
    --green-bright: #33ad60;
    --edge-light: rgba(255, 255, 255, 0.55);
    --brand-ink: #1d4a38;
  }
  * { margin: 0; padding: 0; box-sizing: border-box; }
  html, body {
    width: 1200px;
    height: 900px;
    overflow: hidden;
    background: var(--paper);
  }
  .slide {
    position: relative;
    width: 1200px;
    height: 900px;
    overflow: hidden;
    background: var(--paper);
  }
  .micro-texture {
    position: absolute;
    left: 0;
    top: 0;
    width: 560px;
    height: 700px;
    background: radial-gradient(ellipse at 20% 25%, #d6d8d7 0%, var(--mist) 40%, rgba(255,255,255,0) 80%);
  }
  .footer-band {
    position: absolute;
    left: 0;
    bottom: 0;
    width: 1200px;
    height: 57px;
    background: var(--footer-band);
  }
  .sweep {
    position: absolute;
    left: 0;
    top: 0;
    width: 1200px;
    height: 900px;
  }
  .brand {
    position: absolute;
    left: 66px;
    top: 728px;
    display: flex;
    align-items: center;
    gap: 12px;
    font-family: "Roboto", Arial, sans-serif;
    font-weight: 700;
    color: var(--brand-ink);
  }
  .brand-dot {
    width: 26px;
    height: 26px;
    border-radius: 50%;
    background: var(--green-bright);
  }
  .brand-name {
    font-size: 42px;
    letter-spacing: 1px;
    line-height: 1;
  }
  .brand-sub {
    display: block;
    font-size: 22px;
    letter-spacing: 1px;
    margin-top: 6px;
    margin-left: 128px;
  }
</style>
</head>
<body>
  <main class="slide">
    <div class="micro-texture" role="img" aria-label="Faint grey microscope view of rod-shaped bacteria on a fibrous surface"></div>
    <div class="footer-band"></div>

    <svg class="sweep" viewBox="0 0 1200 900" aria-hidden="true">
      <path d="M132,0 C170,420 470,750 800,900 L1200,900 L1200,0 Z" fill="var(--green-deep)"/>
      <path d="M275,0 C300,390 560,720 900,900 L1200,900 L1200,0 Z" fill="var(--green-mid)" stroke="var(--edge-light)" stroke-width="2"/>
      <path d="M395,0 C420,370 660,700 1010,900 L1200,900 L1200,0 Z" fill="var(--green-bright)" stroke="var(--edge-light)" stroke-width="2"/>
      <rect x="0" y="0" width="1200" height="38" fill="#ffffff" opacity="0.1"/>
    </svg>

    <div class="brand">
      <span class="brand-dot"></span>
      <div>
        <span class="brand-name">VELORIN</span>
        <span class="brand-sub">Biotech</span>
      </div>
    </div>
  </main>
</body>
</html>
```